Business Card Design

My business will be called TB Joinery & Renovations. I am a liscenced carpentar who specialises in renovations/alterations/refurbishments and maintenance. I have experience in all types of Carpentry tho. I also have experience in tiling, painting and concrete which obviously gives me an edge in the refurbishment market for building. But i am not liscenced in these trades. I pride myself on being an honest and very reliable. There are alot of tradesman where i live who are not reliable so i really want to let the community know they can trust me and that i am willing to do all types of work.
I would like to see design and is not over the top but uses earthy/modern colours which presents a down to earth message.

I would really like to communicate diversity, reliabilty and quality work.

I have attached a couple of concepts i have come up with PaperKite, These may aid you.

Industry/Entity Type

Painting

Contact Information for Business Card

Name: Dean Wolworth
Email: dean.wolw@postlark.net
Ph: 0418529364

Requirements
Must have
• Licence No: 318827K

```html
<!DOCTYPE html>
<html lang="en">
<head>
<meta charset="utf-8">
<title>TB Joinery &amp; Renovations – Business Card</title>
<link rel="stylesheet" href="https://fonts.googleapis.com/css2?family=Bree+Serif&family=Open+Sans:wght@400&display=swap">
<style>
  :root {
    --page-bg: #d9d4cc;
    --card-bg: #ebe8e3;
    --ink-brown: #5b4232;
    --ink-body: #5e5650;
    --icon: #5a4c43;
    --rule: #a39a92;
    --wood-dark: #3f3a35;
    --wood-mid: #5a534c;
    --wood-light: #6b635b;
    --edge-light: #f7f5f1;
  }
  * { box-sizing: border-box; margin: 0; padding: 0; }
  html, body {
    width: 1200px; height: 798px; overflow: hidden;
    background: var(--page-bg);
  }
  .canvas {
    position: relative; width: 1200px; height: 798px;
  }
  .card {
    position: absolute;
    width: 540px; height: 310px;
    background: var(--card-bg);
    overflow: hidden;
    box-shadow: 0 6px 18px rgba(0,0,0,0.18);
  }
  .card--front { left: 40px; top: 244px; }
  .card--back { left: 620px; top: 244px; }

  .wood-strip {
    position: absolute; left: 0; right: 0; bottom: 0;
    background: linear-gradient(180deg, var(--wood-mid), var(--wood-dark) 55%, var(--wood-light));
    border-top: 3px solid var(--edge-light);
  }
  .card--front .wood-strip { height: 112px; }
  .card--back .wood-strip { height: 52px; }

  .brand {
    position: absolute; left: 0; right: 0; top: 62px;
    text-align: center;
    font-family: "Bree Serif", serif;
    font-weight: 400;
    color: var(--ink-brown);
    line-height: 1.05;
  }
  .brand__line1 { display: block; font-size: 40px; }
  .brand__line2 { display: block; font-size: 40px; }
  .brand__amp { font-size: 28px; }

  .holder {
    position: absolute; right: 40px; top: 34px;
    font-family: "Bree Serif", serif;
    font-weight: 400;
    font-size: 30px; color: var(--ink-brown);
  }
  .holder-rule {
    position: absolute; left: 40px; right: 40px; top: 80px;
    height: 1px; background: var(--rule);
  }
  .contact-list {
    position: absolute; left: 50px; top: 96px;
    list-style: none;
    font-family: "Open Sans", sans-serif;
    font-size: 17px; color: var(--ink-body);
  }
  .contact-list li {
    display: flex; align-items: center; gap: 16px;
    height: 36px; white-space: nowrap;
  }
  .contact-list svg { width: 20px; height: 20px; fill: var(--icon); flex: none; }
</style>
</head>
<body>
<div class="canvas">

  <section class="card card--front">
    <h1 class="brand">
      <span class="brand__line1">TB Joinery</span>
      <span class="brand__line2"><span class="brand__amp">&amp;</span> Renovations</span>
    </h1>
    <div class="wood-strip" role="img" aria-label="Dark timber floorboards with a wrench set, a hand saw and a hammer laid across them"></div>
  </section>

  <section class="card card--back">
    <h2 class="holder">Dean Wolworth</h2>
    <div class="holder-rule"></div>
    <ul class="contact-list">
      <li>
        <svg viewBox="0 0 20 20" aria-hidden="true"><path d="M1 4h18v12H1z M2.5 5.5 10 11l7.5-5.5v-.5h-15z" fill-rule="evenodd"/></svg>
        <span>dean.wolw@postlark.net</span>
      </li>
      <li>
        <svg viewBox="0 0 20 20" aria-hidden="true"><path d="M5 1h10a1 1 0 0 1 1 1v16a1 1 0 0 1-1 1H5a1 1 0 0 1-1-1V2a1 1 0 0 1 1-1zm1 2v12h8V3zm4 13a1 1 0 1 0 0 2 1 1 0 0 0 0-2z" fill-rule="evenodd"/></svg>
        <span>0418529364</span>
      </li>
      <li>
        <svg viewBox="0 0 20 20" aria-hidden="true"><path d="M10 1a6 6 0 0 1 6 6c0 4.5-6 12-6 12S4 11.5 4 7a6 6 0 0 1 6-6zm0 3.5a2.5 2.5 0 1 0 0 5 2.5 2.5 0 0 0 0-5z" fill-rule="evenodd"/></svg>
        <span>57 Ridgeway Road, Ballarat, Australia</span>
      </li>
      <li>
        <svg viewBox="0 0 20 20" aria-hidden="true"><path d="M10 1a9 9 0 1 1 0 18 9 9 0 0 1 0-18zm4.3 5.3L8.6 12 5.7 9.1 4.3 10.5l4.3 4.3 7.1-7.1z" fill-rule="evenodd"/></svg>
        <span>Licence No: 318827K</span>
      </li>
    </ul>
    <div class="wood-strip" role="img" aria-label="Dark timber floorboards band"></div>
  </section>

</div>
</body>
</html>
```